'Brindle e@sy' Initial leaflet

I need an A5 Leaflet designed to launch the new service we are offering.
Currently we operate a traditional estate agency based in the uk that covers sales and letting of property.

The working name for the new service is 'Brindle e@sy'

We are starting a new offering that will be an online offering for the local area. Similar to 'Tealhouse' but with an actual local face and office.
I need the leaflet to promote this.
The leaflet must be modern, informative and in our corporate colours. I have attached some logos and previous leaflets that we have had to show colours etc.
The main points to detail on the leaflet will be that
we offer an Online Service
Its a lower price
We still offer the local office/face.
Professional Photos Included
Floorplans Included

The price we will offer this service at will be 'From £795 inc VAT'

Id like to have an offer on the leaflet that instruction received in September/October 2018 will get the service for reduced price of £600 Including VAT.

I look forward to seeing what we get!

Martin

Requirements
Must have
• Must be double sided! Should be attractive and modern.

```html
<!DOCTYPE html>
<html lang="en">
<head>
<meta charset="utf-8">
<title>Brindle Estate Agents – Leaflet</title>
<link href="https://fonts.googleapis.com/css2?family=Tinos:wght@400;700&family=Open+Sans:wght@400;600&family=Archivo+Black&family=Archivo:wght@700&display=swap" rel="stylesheet">
<style>
:root{
  --orange:#ef5134;
  --black:#0d0d0d;
  --ink:#1a1a1a;
  --grey:#8a8a8a;
  --light:#bdbdbd;
  --white:#ffffff;
  --backdrop:#e9e9e9;
  --footer-dark:#2b2b2b;
}
*{box-sizing:border-box;margin:0;padding:0}
html,body{width:1200px;height:793px;overflow:hidden;background:var(--backdrop)}
body{position:relative;font-family:'Open Sans',sans-serif}
.page{position:absolute;top:45px;width:484px;height:685px;background:var(--black);overflow:hidden;box-shadow:0 2px 8px rgba(0,0,0,.25)}
.page--front{left:98px}
.page--back{left:606px}
.shapes{position:absolute;inset:0;width:484px;height:685px}
.abs{position:absolute}
.serif{font-family:'Tinos',serif}
.brand-name{font-family:'Tinos',serif;color:var(--orange);font-weight:400;line-height:1;white-space:nowrap}
.brand-sub{font-family:'Tinos',serif;color:var(--orange);font-size:13px;white-space:nowrap}
.brand-dot{position:absolute;border-radius:50%;background:var(--orange);border:3px solid var(--white)}
.center{text-align:center;left:0;width:484px}
.welcome{top:300px;font-size:35px;color:var(--grey)}
.welcome-title{top:349px;font-size:38px;color:var(--orange);font-weight:700}
.rule{position:absolute;left:227px;top:396px;width:30px;height:2px;background:var(--white)}
.intro{top:406px;left:70px;width:344px;font-size:10.5px;line-height:14.5px;color:var(--light);text-align:center}
.feature-box{position:absolute;left:27px;top:483px;width:432px;height:99px;border:1px solid var(--grey)}
.icon-circle{position:absolute;width:64px;height:64px;border-radius:50%;background:var(--orange);border:2px solid var(--white);display:flex;align-items:center;justify-content:center}
.feature{position:absolute;width:130px;text-align:center}
.feature h3{font-family:'Tinos',serif;font-weight:400;font-size:11px;color:var(--orange);margin-bottom:3px}
.feature p{font-size:6.2px;line-height:8.4px;color:var(--white)}
.offer-line{left:18px;top:593px;font-family:'Archivo',sans-serif;font-weight:700;font-size:14px;color:var(--white)}
.offer-price{left:18px;top:611px;font-family:'Tinos',serif;font-weight:700;font-size:22px;color:var(--orange)}
.price-pill{position:absolute;left:256px;top:593px;width:210px;height:38px;border:1px solid var(--white);border-radius:19px;font-family:'Tinos',serif;font-weight:700;font-size:10.5px;line-height:14px;color:var(--orange);padding:6px 0 0 14px}
.price-pill b{color:var(--white)}
.footer{position:absolute;left:0;top:646px;width:484px;height:39px}
.phone{position:absolute;left:19px;top:2px;font-family:'Archivo Black',sans-serif;font-size:23px;color:var(--white);letter-spacing:.5px;line-height:26px}
.hours{position:absolute;left:19px;top:27px;font-family:'Archivo',sans-serif;font-weight:700;font-size:8.6px;letter-spacing:1.4px;color:var(--white)}
.web{position:absolute;right:14px;top:28px;font-family:'Tinos',serif;font-size:8px;color:var(--white)}
.offer-text{top:155px;font-size:17.5px;line-height:22px;color:#6f6f6f}
.offer-text strong{color:var(--orange)}
.perk{position:absolute;width:140px;text-align:center;font-family:'Tinos',serif;font-weight:700;font-size:13px;line-height:16.5px;color:var(--white)}
.about-title{top:384px;font-size:38px;color:var(--grey)}
.about{position:absolute;left:58px;top:446px;width:370px;font-size:9.2px;line-height:13px;color:var(--light)}
.about p{margin-bottom:13px}
.about ul{list-style:none}
.about li{position:relative}
.about li::before{content:"";position:absolute;left:-16px;top:3px;width:7px;height:7px;border-radius:50%;background:var(--orange)}
</style>
</head>
<body>

<!-- FRONT -->
<section class="page page--front" aria-label="Leaflet front page">
  <svg class="shapes" viewBox="0 0 484 685" aria-hidden="true">
    <path d="M0 95 C150 150 330 150 484 78 V640 H0 Z" fill="#5d7b3f"/>
    <path d="M0 0 H484 V80 C330 150 150 150 0 95 Z" fill="var(--black)"/>
    <path d="M0 95 C150 150 330 150 484 78 V92 C330 165 140 165 0 108 Z" fill="var(--orange)"/>
    <path d="M0 108 C140 165 330 165 484 92 V98 C330 172 140 172 0 114 Z" fill="var(--white)"/>
    <path d="M110 130 C240 175 380 150 484 98 V104 C380 158 240 182 110 130 Z" fill="var(--black)"/>
    <path d="M0 345 C140 290 330 270 484 300 V685 H0 Z" fill="var(--black)"/>
    <path d="M0 328 C140 275 330 255 484 282 V300 C330 270 140 290 0 345 Z" fill="var(--orange)"/>
    <path d="M0 318 C140 265 330 245 484 268 V282 C330 255 140 275 0 328 Z" fill="var(--white)"/>
    <path d="M60 335 C200 285 360 275 484 300 V312 C360 290 200 300 60 335 Z" fill="#3a3a3a"/>
  </svg>
  <div class="abs" role="img" aria-label="Aerial photograph of the local town: roundabout, green lawns, trees and office buildings" style="left:0;top:110px;width:484px;height:190px;background:linear-gradient(180deg,#dfe8ef 0%,#c8d6de 28%,#7d8f6a 45%,#5a7a3e 70%,#6c6f6a 100%);clip-path:polygon(0 0,100% 0,100% 100%,0 100%);z-index:0;opacity:0"></div>

  <span class="brand-dot" style="left:106px;top:26px;width:72px;height:72px"></span>
  <div class="abs brand-name" style="left:192px;top:30px;font-size:56px">Brindle</div>
  <div class="abs brand-sub" style="left:292px;top:78px">Estate Agents</div>

  <div class="abs center serif welcome">Welcome to</div>
  <div class="abs center serif welcome-title">Brindle Estate Agents</div>
  <span class="rule"></span>
  <p class="abs intro">Brindle Estate Agents specialise in residential sales, lettings and property management. Our experienced team can advise you on just about everything from decor to financial advice, we have it covered!</p>

  <div class="feature-box"></div>
  <div class="icon-circle" style="left:67px;top:455px">
    <svg width="36" height="34" viewBox="0 0 36 34"><path d="M18 2 L34 16 H29 V32 H21 V22 H15 V32 H7 V16 H2 Z" fill="var(--black)"/></svg>
  </div>
  <div class="icon-circle" style="left:209px;top:455px">
    <svg width="34" height="34" viewBox="0 0 34 34"><path d="M24 3 L31 10 L12 29 L3 31 L5 22 Z" fill="var(--black)"/><path d="M21 6 L28 13" stroke="var(--orange)" stroke-width="2"/></svg>
  </div>
  <div class="icon-circle" style="left:359px;top:455px">
    <svg width="30" height="34" viewBox="0 0 30 34"><circle cx="15" cy="11" r="9" fill="var(--black)"/><rect x="13.5" y="9" width="3" height="8" fill="var(--orange)"/><circle cx="15" cy="6" r="1.7" fill="var(--orange)"/><path d="M3 33 C3 24 27 24 27 33 Z" fill="var(--black)"/></svg>
  </div>
  <div class="feature" style="left:34px;top:525px"><h3>What's Your Home Worth?</h3><p>Try our instant online valuation tool and find out what your home could be worth in as little as 60 seconds.</p></div>
  <div class="feature" style="left:176px;top:525px"><h3>Register With Us</h3><p>Want to stay up to date with properties you might be interested in? Register with us to receive regular property updates</p></div>
  <div class="feature" style="left:326px;top:525px"><h3>Ask an Expert</h3><p>Do you have a property related question? Click here to ask your local expert!</p></div>

  <div class="abs offer-line">WE OFFER AN ONLINE SERVICE</div>
  <div class="abs offer-price">ITS A LOWER PRICE</div>
  <div class="price-pill">WE WILL OFFER THIS SERVICE<br>AT WILL BE FROM <b>£795 INC VAT</b></div>

  <div class="footer">
    <svg class="abs" width="484" height="39" viewBox="0 0 484 39" aria-hidden="true" style="left:0;top:0"><rect width="484" height="39" fill="var(--footer-dark)"/><path d="M0 0 H320 C330 0 334 14 340 39 H0 Z" fill="var(--orange)"/></svg>
    <div class="phone">PHONE : 01632 960500</div>
    <div class="hours">LINES ARE OPEN 8AM TO 9PM, 7 DAYS A WEEK!</div>
    <div class="web">www.brindleestateagents.co.uk</div>
  </div>
</section>

<!-- BACK -->
<section class="page page--back" aria-label="Leaflet back page">
  <svg class="shapes" viewBox="0 0 484 685" aria-hidden="true">
    <rect x="0" y="100" width="484" height="138" fill="var(--white)"/>
    <path d="M0 0 H484 V80 C300 100 120 120 0 160 Z" fill="var(--black)"/>
    <path d="M0 160 C120 120 300 100 484 80 V92 C300 110 120 135 0 175 Z" fill="var(--orange)"/>
    <path d="M0 175 C120 135 300 110 484 92 V100 C300 118 120 145 0 185 Z" fill="var(--black)"/>
    <rect x="0" y="238" width="484" height="136" fill="var(--orange)"/>
  </svg>
  <div class="abs brand-name" style="left:137px;top:6px;font-size:62px">Brindle</div>
  <div class="abs brand-sub" style="left:238px;top:60px">Estate Agents</div>
  <span class="brand-dot" style="left:356px;top:18px;width:134px;height:134px;border-color:var(--black);box-shadow:0 0 0 2px var(--white)"></span>

  <p class="abs center serif offer-text">An offer on the leaflet that instruction received<br>in September/October 2018 will get the service for<br>reduced price of <strong>£600 Including VAT</strong>.</p>

  <span class="brand-dot" style="left:66px;top:247px;width:64px;height:64px;background:var(--black)"></span>
  <span class="brand-dot" style="left:208px;top:247px;width:64px;height:64px;background:var(--black)"></span>
  <span class="brand-dot" style="left:357px;top:247px;width:64px;height:64px;background:var(--black)"></span>
  <div class="perk" style="left:28px;top:321px">FREE<br>FLOOR PLANS</div>
  <div class="perk" style="left:170px;top:321px">FREE<br>VIDEO TOURS</div>
  <div class="perk" style="left:309px;top:316px;width:160px">FREE<br>PROFESSIONALLY<br>ENHANCED PHOTOS</div>

  <h2 class="abs center serif about-title" style="font-weight:400">About Us</h2>
  <div class="about">
    <p>Brindle Estate Agents' aim is to give each client everything they need to help them along their property 'journey'. We will strive to give you the highest standard of service available and customer satisfaction is our priority.</p>
    <p>At Brindle Estate Agents we promise to do everything we can to help you during the process of selling your home. We have a number of service standards that we will provide, these include:</p>
    <ul>
      <li>Free Valuations</li>
      <li>Market research to help you choose the right price for your property</li>
      <li>All feedback given within 24 hours</li>
      <li>Regular Updates on the market and advice on how to stay ahead of the competition</li>
      <li>Plus we offer help finding qualified professionals for services including mortgage advice, property conveyancing and insurance.</li>
    </ul>
  </div>

  <div class="footer">
    <svg class="abs" width="484" height="39" viewBox="0 0 484 39" aria-hidden="true" style="left:0;top:0"><rect width="484" height="39" fill="var(--footer-dark)"/><path d="M0 0 H320 C330 0 334 14 340 39 H0 Z" fill="var(--orange)"/></svg>
    <div class="phone">PHONE : 01632 960500</div>
    <div class="hours">LINES ARE OPEN 8AM TO 9PM, 7 DAYS A WEEK!</div>
    <div class="web">www.brindleestateagents.co.uk</div>
  </div>
</section>

</body>
</html>
```